Harvest Gate Fellowship Network needs a fresh new web design

We are an up and coming multicultural church that aims to bring people into a life changing encounter with God. We need a fresh and inviting website in order to increase our internet presence and make us easier to connect with.
Here are some of the basic requirements for the site:
• Clearly displayed address, service times, and contact info
• A staff profile page
• An area for a calendar with upcoming events and their details
• Social media buttons
• Group pages for the different ministries (youth, children’s church, men, etc…)
• An area for donations and eCommerce
• A resources page for assorted media (podcasts, sermons, videos, etc.…)
• An area for prayer requests.

Industry/Entity Type

Church

```html
<!DOCTYPE html>
<html lang="en">
<head>
<meta charset="utf-8">
<title>Harvest Gate Fellowship Network</title>
<link href="https://fonts.googleapis.com/css2?family=Open+Sans:wght@400;600;700&display=swap" rel="stylesheet">
<style>
:root{
  --blue:#07609a;
  --blue-dark:#0a5488;
  --band:#065f93;
  --ink:#333;
  --muted:#666;
  --footer:#c8c8c8;
  --line:#d6d6d6;
  --btn-light:#d9d9d9;
  --white:#fff;
}
*{margin:0;padding:0;box-sizing:border-box}
html,body{width:942px;height:1200px;overflow:hidden;background:var(--white)}
body{position:relative;font-family:"Open Sans",Arial,sans-serif;color:var(--ink)}
.abs{position:absolute}
/* header */
.brand{left:196px;top:28px;display:flex;align-items:center;gap:6px;font-size:13px;font-weight:700;color:var(--blue);line-height:1.15;width:150px}
.brand-dot{width:12px;height:12px;border-radius:50%;background:#e9b423;flex:none}
.nav{top:36px;left:392px;display:flex;font-size:11px;color:#444}
.nav span{padding:0 10px;border-left:1px solid #bbb;line-height:16px}
.nav span:first-child{border-left:0;color:var(--blue)}
/* blue band */
.band{left:0;top:83px;width:942px;height:441px;background:var(--band);border-top:1px solid #9bb}
.hero{left:176px;top:84px;width:590px;height:222px;background:linear-gradient(135deg,#c9a08f 0%,#e3bba8 45%,#f1d8c8 75%,#f6ede6 100%)}
.caption{left:470px;top:171px;width:296px;height:59px;background:rgba(40,30,26,.85);color:var(--white);font-size:13.5px;line-height:19px;padding:9px 0 0 53px}
.dots{left:190px;top:287px;display:flex;gap:2px}
.dots i{width:6px;height:6px;background:#555}
.dots i:first-child{background:var(--blue)}
.h-white{color:var(--white);font-size:11.5px;font-weight:700}
.copy{font-size:8.2px;line-height:13.2px;text-align:justify}
.copy.light{color:var(--white)}
.btn{height:18px;font-size:7.6px;display:flex;align-items:center;justify-content:center}
.btn.light{background:var(--btn-light);color:#333}
.btn.dark{background:var(--blue);color:var(--white)}
.staff-photo{width:45px;height:40px;background:linear-gradient(#e8e8e8,#9a8f88)}
.staff-text{font-size:8.2px;line-height:13.2px;color:var(--white);width:105px}
/* middle */
.rule{left:0;top:526px;width:942px;height:1px;background:var(--line)}
.h-blue{color:var(--blue);font-size:11.5px;font-weight:700}
.divider{left:176px;top:730px;width:414px;height:1px;background:#ccc}
.cal{left:621px;top:578px;width:139px}
.cal-head{background:var(--blue);height:17px;color:var(--white);font-size:7px;font-weight:700;display:flex;align-items:center;justify-content:space-between;padding:0 22px}
.cal-body{background:#ececec;padding:6px 4px 4px}
.cal table{width:100%;border-collapse:collapse;font-size:6.3px;text-align:center;color:#555}
.cal th{font-weight:700;color:#333;padding-bottom:6px}
.cal td{height:10.6px}
.cal td.on{background:var(--blue);color:var(--white);font-weight:700}
.evt-date{width:37px;height:36px;background:#ececec;font-size:8.5px;color:#444;text-align:center;line-height:15px;padding-top:3px}
.evt-text{width:96px;font-size:8.2px;line-height:12.6px;color:var(--ink)}
.donate{left:623px;top:829px;width:143px;height:63px;background:linear-gradient(120deg,#3aaad6,#7fd0ea 70%,#eac4c8);}
.donate-label{left:630px;top:836px;color:var(--white);font-size:11px;line-height:12px;font-weight:600}
/* footer */
.foot{left:0;top:934px;width:942px;height:200px;background:var(--footer);border-top:2px solid #ddd}
.vline{top:936px;width:1px;height:198px;background:#e4e4e4}
.f-h{font-size:10.5px;color:#333}
.f-item{font-size:8.2px;color:#555}
.input{left:593px;width:142px;height:18px;background:var(--white);font-size:7.2px;color:#777;padding:4px 0 0 12px}
.send{left:593px;top:1090px;width:50px;height:22px;background:var(--blue-dark);color:var(--white);font-size:10px;font-weight:700;border-radius:3px;display:flex;align-items:center;justify-content:center}
.links{left:176px;top:1153px;font-size:8.2px;color:#666}
.legal{left:176px;top:1171px;font-size:8.2px;color:#666}
.social{left:610px;top:1157px;display:flex;gap:3px}
.social i{width:23px;height:23px;background:var(--blue-dark);display:block}
</style>
</head>
<body>
<header>
  <div class="abs brand"><span class="brand-dot"></span><span>Harvest Gate Fellowship Network</span></div>
  <nav class="abs nav"><span>Home</span><span>Aabout Us</span><span>Events</span><span>Prayer Request</span><span>Donate</span><span>Contacts</span></nav>
</header>

<section>
  <div class="abs band"></div>
  <div class="abs hero" role="img" aria-label="Photo of an elderly hand resting in a younger hand"></div>
  <div class="abs caption">No limits, No Boundaries,<br>but increase in Jesus name</div>
  <div class="abs dots"><i></i><i></i><i></i><i></i></div>

  <h2 class="abs h-white" style="left:177px;top:332px">Welcome to HGFN</h2>
  <div class="abs" role="img" aria-label="Photo of hands folded in prayer over an open bible" style="left:176px;top:359px;width:138px;height:96px;background:linear-gradient(120deg,#e6dccb,#8c5a2e 55%,#3a2312)"></div>
  <p class="abs copy light" style="left:326px;top:358px;width:247px">Welcome to Harvest Gate Fellowship Network, a place where we can come together and fellowship. HGFN is located in Riverside, Ohio and we would love to have you worship with us. We believe God is doing something extraordinary through our church and would like for you to be a part. Please prayerfully consider our church as a place you would like to worship and fellowship with us as we continue to grow.</p>
  <div class="abs btn light" style="left:177px;top:472px;width:61px">Read More</div>

  <h2 class="abs h-white" style="left:606px;top:332px">Staff Profile</h2>
  <div class="abs staff-photo" role="img" aria-label="Portrait of a male pastor" style="left:604px;top:362px"></div>
  <p class="abs staff-text" style="left:660px;top:358px">Marcus Ellery is a native of the Caribbean island of Jamaica and strongly</p>
  <div class="abs staff-photo" role="img" aria-label="Portrait of a female minister" style="left:604px;top:414px"></div>
  <p class="abs staff-text" style="left:660px;top:411px">Marcus Ellery is a native of the Caribbean island of Jamaica and strongly</p>
  <div class="abs btn light" style="left:603px;top:472px;width:62px">Read More</div>
</section>

<div class="abs rule"></div>

<section>
  <h2 class="abs h-blue" style="left:177px;top:550px">Group ministries</h2>
  <div class="abs" role="img" aria-label="Photo of open hands raised against a dark background" style="left:176px;top:582px;width:138px;height:96px;background:radial-gradient(ellipse at 50% 60%,#b5704a,#3a1a0c 45%,#000 75%)"></div>
  <p class="abs copy" style="left:331px;top:582px;width:256px">Welcome to Harvest Gate Fellowship Network, a place where we can come together and fellowship. HGFN is located in Riverside, Ohio and we would love to have you worship with us. We believe God is doing something extraordinary through our church and would like for you to be a part. Please prayerfully consider our church as a place you would like to worship and fellowship with us as we continue to grow.</p>
  <div class="abs btn dark" style="left:177px;top:694px;width:61px">Read More</div>
  <div class="abs divider"></div>

  <h2 class="abs h-blue" style="left:177px;top:741px">Media</h2>
  <div class="abs" role="img" aria-label="Video still of a person with hands clasped in prayer" style="left:178px;top:773px;width:195px;height:129px;background:radial-gradient(ellipse at 50% 55%,#6a6a6a,#2a2a2a 55%,#111)"></div>
  <svg class="abs" style="left:178px;top:884px" width="195" height="18" viewBox="0 0 195 18">
    <rect width="195" height="18" fill="#111"/>
    <rect x="3" y="2" width="26" height="14" fill="#222"/>
    <path d="M13 5 L20 9 L13 13Z" fill="#fff"/>
    <rect x="36" y="8" width="122" height="3" fill="#1e8fd0"/>
    <rect x="162" y="7" width="14" height="5" fill="#1e8fd0"/>
    <rect x="182" y="7" width="5" height="5" fill="#ccc"/>
  </svg>
  <p class="abs copy" style="left:400px;top:767px;width:187px">Welcome to Harvest Gate Fellowship Network, a place where we can come together and fellowship. HGFN is located in Riverside, Ohio and we would love to have you worship with us. We believe God is doing something extraordinary through our church and would like for you to be a part. Please prayerfully consider our church as a place you would like to worship and fellowship with us as we continue to grow. As you venture on our website please feel free to contact</p>

  <h2 class="abs h-blue" style="left:622px;top:551px">Upcoming Events</h2>
  <div class="abs cal">
    <div class="cal-head"><span>&#9664;</span><span>JUNE 2014</span><span>&#9654;</span></div>
    <div class="cal-body">
      <table>
        <tr><th>Su</th><th>Mo</th><th>Tu</th><th>We</th><th>Th</th><th>Fr</th><th>Sa</th></tr>
        <tr><td></td><td></td><td></td><td></td><td>1</td><td>2</td><td>3</td></tr>
        <tr><td>4</td><td>5</td><td>6</td><td>7</td><td>8</td><td>9</td><td>10</td></tr>
        <tr><td>11</td><td>12</td><td>13</td><td>14</td><td>15</td><td>16</td><td>17</td></tr>
        <tr><td>18</td><td>19</td><td>20</td><td>21</td><td>22</td><td>23</td><td>24</td></tr>
        <tr><td>25</td><td>26</td><td>27</td><td>28</td><td class="on">29</td><td>30</td><td>31</td></tr>
      </table>
    </div>
  </div>
  <div class="abs evt-date" style="left:622px;top:694px">29<br>Jan</div>
  <p class="abs evt-text" style="left:670px;top:692px">Marcus Ellery is a native of he Caribbean island of Jamaica and strongly</p>
  <div class="abs evt-date" style="left:622px;top:746px">02<br>Feb</div>
  <p class="abs evt-text" style="left:670px;top:743px">Marcus Ellery is a native of he Caribbean island of Jamaica and strongly</p>
  <div class="abs btn dark" style="left:622px;top:791px;width:61px">Read More</div>
  <div class="abs donate" role="img" aria-label="Donation banner with a coin dropping into a piggy bank"></div>
  <div class="abs donate-label">Make a<br>donation</div>
</section>

<footer>
  <div class="abs foot"></div>
  <div class="abs vline" style="left:355px"></div>
  <div class="abs vline" style="left:562px"></div>

  <h3 class="abs f-h" style="left:182px;top:966px;font-weight:400">Contact Us</h3>
  <span class="abs f-item" style="left:184px;top:992px">Address</span>
  <span class="abs f-item" style="left:184px;top:1015px">Street Name</span>
  <svg class="abs" style="left:184px;top:1039px" width="11" height="9" viewBox="0 0 11 9"><rect x=".5" y=".5" width="10" height="8" fill="none" stroke="#0a5488"/><path d="M.5 .5 L5.5 5 L10.5 .5" fill="none" stroke="#0a5488"/></svg>
  <span class="abs f-item" style="left:199px;top:1037px">info@harvestgatefn.org</span>
  <svg class="abs" style="left:184px;top:1058px" width="9" height="13" viewBox="0 0 9 13"><rect x=".75" y=".75" width="7.5" height="11.5" rx="1" fill="none" stroke="#0a5488" stroke-width="1.5"/></svg>
  <span class="abs f-item" style="left:199px;top:1060px">555.014.2290</span>

  <h3 class="abs f-h" style="left:398px;top:966px;font-weight:400">Service Times</h3>
  <span class="abs f-item" style="left:397px;top:992px">Monday</span><span class="abs f-item" style="left:453px;top:992px">@ 9am to 10 pm</span>
  <span class="abs f-item" style="left:397px;top:1015px">Tuesday</span><span class="abs f-item" style="left:452px;top:1015px">@ 9am to 10 pm</span>
  <span class="abs f-item" style="left:397px;top:1037px">Wednesday</span><span class="abs f-item" style="left:453px;top:1037px">@ 9am to 10 pm</span>
  <span class="abs f-item" style="left:397px;top:1060px">Friday</span><span class="abs f-item" style="left:453px;top:1060px">@ 9am to 10 pm</span>
  <span class="abs f-item" style="left:397px;top:1083px">Sunday</span><span class="abs f-item" style="left:453px;top:1083px">@ 9am to 10 pm</span>

  <h3 class="abs f-h" style="left:594px;top:966px;font-weight:400">Prayer Request</h3>
  <div class="abs input" style="top:992px">Name</div>
  <div class="abs input" style="top:1016px">Email</div>
  <div class="abs input" style="top:1040px">Prayer Topic</div>
  <svg class="abs" style="left:719px;top:1046px" width="8" height="6" viewBox="0 0 8 6"><path d="M0 0 L8 0 L4 6Z" fill="#aaa"/></svg>
  <div class="abs input" style="top:1064px">Prayer Request</div>
  <div class="abs send">Send</div>

  <div class="abs links">Home &nbsp;|&nbsp; About Us &nbsp;|&nbsp; Events &nbsp;|&nbsp; Prayer Request &nbsp;|&nbsp; Donate &nbsp;|&nbsp; Contact Us</div>
  <div class="abs legal">harvestgatefn.org &nbsp;© 2014 &nbsp;|&nbsp; Privacy Policy</div>
  <div class="abs social" aria-label="Social media links"><i></i><i></i><i></i><i></i><i></i></div>
</footer>
</body>
</html>
```